Modern Yoga Studio Timetable and Flyer Design

We have a comprehensive class timetable and we are wanting to a clean modern look for our Spring timetable.

We require a double sided flyer with our class timetable included.
We would prefer an A5 size (postcard) or DL (1/3 A4).

We would like the final flyer to have.
Side A : Yoga image, logo

Fennel Stretch Hall
address: 4/71 Wexcombe Lane, Pelharton
website: fennelstretch.com.au
mobile: 0471 296 814

Side B: Clear easy to read timetable with a break down of class types and website.

We would also like to have a copy of the timetable itself as a separate jpg or pdf for use on our website to download.

Thank you.
Yours kindly,
Nell

I have attached a sample of another timetable of which I like the look and feel of, however this is just a guide. I've also attached our 'new' schedule in WORD plus uploaded our last design of the front.
Updates

Target Market(s)

Women aged 30-45

Industry/Entity Type

Health And Wellness

Font styles to use
Other font styles liked:
• Brandon Grotesque, Jenna Sue

Colors
6c459b
33a6d7
ffffff

Requirements
Must have
• A definitive colour to decipher between different class types on our timetable. Where each colour represents a different class type. Colours and layouts similar to our website design, see www.fennelstretch.com.au
Nice to have
• I've included a design of another studio whose timetable design I like. One of our own yoga images instead of a stock image.
Should not have
• No dark gridlines between the cells/boxes in the timetables. Please don't use stock yoga images.

```html
<!DOCTYPE html>
<html lang="en">
<head>
<meta charset="utf-8">
<title>Fennel Stretch Hall – Spring Flyer</title>
<link href="https://fonts.googleapis.com/css2?family=Caveat:wght@500&family=Montserrat:wght@500;800&family=Lato:wght@400;700&display=swap" rel="stylesheet">
<style>
  :root {
    --purple: #6c459b;
    --purple-dark: #4a2a7a;
    --purple-soft: #9b86c1;
    --lavender: #d9d1ea;
    --ice: #e8eef6;
    --blue: #33a6d7;
    --white: #ffffff;
    --ink: #2b2b2b;
    --backdrop: #ebe6e0;
    /* class type colours */
    --type-flow: #c9b6e6;
    --type-gentle: #b5dff1;
    --type-prenatal: #f4c6dc;
    --type-youth: #c5e6b8;
    --type-special: #f6dfa6;
  }
  * { margin: 0; padding: 0; box-sizing: border-box; }
  html, body { width: 1200px; height: 907px; overflow: hidden; }
  body { position: relative; background: var(--backdrop); font-family: "Lato", sans-serif; }

  /* ---------- Side A: flyer front ---------- */
  .flyer-front {
    position: absolute; left: 48px; top: 62px; width: 372px; height: 768px;
    background: var(--white); overflow: hidden;
  }
  .brand-name {
    position: absolute; top: 74px; left: 0; width: 100%; text-align: center;
    font-family: "Montserrat", sans-serif; font-weight: 500; font-size: 22px;
    letter-spacing: 4px; color: var(--blue);
  }
  .studio-photo {
    position: absolute; top: 113px; left: 0; width: 100%; height: 252px;
    background: linear-gradient(180deg, #f1f1ef 0%, #e8e6e3 60%, #b49a78 80%, #9c825f 100%);
  }
  .photo-band {
    position: absolute; top: 368px; left: 0; width: 100%; height: 12px;
    background: var(--purple); border-top: 2px solid var(--white);
  }
  .tagline-script {
    position: absolute; top: 408px; left: 0; width: 100%; text-align: center;
    font-family: "Caveat", cursive; font-weight: 500; font-size: 42px;
    color: var(--purple-dark); line-height: 1;
  }
  .tagline-place {
    position: absolute; top: 456px; left: 0; width: 100%; text-align: center;
    font-family: "Montserrat", sans-serif; font-weight: 500; font-size: 44px;
    color: var(--blue); line-height: 1;
  }
  .call-panel {
    position: absolute; top: 540px; left: 0; width: 100%; height: 100px;
    background: var(--white);
    box-shadow: 0 -6px 8px -6px rgba(0,0,0,0.12), 0 6px 8px -6px rgba(0,0,0,0.12);
    text-align: center;
  }
  .call-label {
    margin-top: 10px; font-family: "Montserrat", sans-serif; font-weight: 800;
    font-size: 28px; letter-spacing: 1px; color: var(--purple-dark);
  }
  .call-number {
    font-family: "Montserrat", sans-serif; font-weight: 500; font-size: 39px;
    color: var(--blue); line-height: 1.1;
  }
  .address-card {
    position: absolute; top: 678px; left: 19px; width: 336px; height: 90px;
    background: var(--purple); border-radius: 14px 14px 0 0;
    color: var(--white); text-align: center;
  }
  .address-name { margin-top: 10px; font-family: "Caveat", cursive; font-size: 22px; }
  .address-line { font-size: 12.5px; line-height: 1.35; display: flex; justify-content: center; align-items: center; gap: 4px; }
  .corner-mark { position: absolute; bottom: 0; width: 16px; height: 14px; background: var(--blue); }
  .corner-mark.left { left: 0; }
  .corner-mark.right { right: 0; }

  /* ---------- Side B: timetable ---------- */
  .timetable-card {
    position: absolute; left: 457px; top: 280px; width: 703px; height: 342px;
    background: var(--white); padding: 10px 21px 0;
  }
  .timetable-title {
    text-align: center; font-weight: 700; font-size: 14px; letter-spacing: 0.6px;
    color: var(--purple); margin-bottom: 8px;
  }
  .timetable { width: 100%; border-collapse: collapse; table-layout: fixed; font-size: 10px; color: var(--ink); }
  .timetable col.time-col { width: 80px; }
  .timetable th {
    background: var(--purple-soft); color: var(--white); font-weight: 400;
    font-size: 11px; height: 20px; text-align: center;
  }
  .timetable td { height: 20.6px; padding: 0 3px; text-align: center; white-space: nowrap; }
  .timetable td.time { text-align: left; padding-left: 10px; color: var(--purple); font-size: 10.5px; }
  .timetable tbody tr:nth-child(odd) { background: var(--ice); }
  .timetable tbody tr:nth-child(even) { background: var(--lavender); }

  .class-tag {
    display: block; border-radius: 8px; padding: 2px 0; line-height: 13px;
    font-size: 10px; color: var(--ink);
  }
  .class-tag.flow { background: var(--type-flow); }
  .class-tag.gentle { background: var(--type-gentle); }
  .class-tag.prenatal { background: var(--type-prenatal); }
  .class-tag.youth { background: var(--type-youth); }
  .class-tag.special { background: var(--type-special); }
</style>
</head>
<body>

<section class="flyer-front">
  <div class="brand-name">Fennel Stretch Hall</div>
  <div class="studio-photo" role="img" aria-label="Photo of a yoga teacher in an extended side angle twist in a bright studio"></div>
  <div class="photo-band"></div>
  <div class="tagline-script">All levels yoga classes</div>
  <div class="tagline-place">in pelharton</div>
  <div class="call-panel">
    <div class="call-label">CALL TODAY</div>
    <div class="call-number">0471 296 814</div>
  </div>
  <div class="address-card">
    <div class="address-name">Fennel Stretch Hall</div>
    <div class="address-line">
      <svg width="9" height="11" viewBox="0 0 10 12" aria-hidden="true"><path d="M5 0a4 4 0 0 0-4 4c0 3 4 8 4 8s4-5 4-8a4 4 0 0 0-4-4zm0 5.5A1.5 1.5 0 1 1 5 2.5a1.5 1.5 0 0 1 0 3z" fill="#fff"/></svg>
      4/71 Wexcombe Lane, Pelharton
    </div>
    <div class="address-line">
      <svg width="8" height="8" viewBox="0 0 10 10" aria-hidden="true"><circle cx="5" cy="5" r="4" fill="none" stroke="#fff" stroke-width="1.4"/></svg>
      www.fennelstretch.com.au
    </div>
  </div>
  <div class="corner-mark left"></div>
  <div class="corner-mark right"></div>
</section>

<section class="timetable-card">
  <h2 class="timetable-title">FENNEL STRETCH SPRING TIMETABLE</h2>
  <table class="timetable">
    <colgroup><col class="time-col"><col><col><col><col><col><col><col></colgroup>
    <thead>
      <tr><th></th><th>MON</th><th>TUE</th><th>WED</th><th>THU</th><th>FRI</th><th>SAT</th><th>SUN</th></tr>
    </thead>
    <tbody>
      <tr><td class="time">5:45am</td><td></td><td><span class="class-tag special">rise + shine*</span></td><td></td><td></td><td></td><td></td><td></td></tr>
      <tr><td class="time">9:00am</td><td></td><td></td><td></td><td></td><td></td><td><span class="class-tag flow">vinyasa flow</span></td><td></td></tr>
      <tr><td class="time">9:15am</td><td></td><td><span class="class-tag flow">vinyasa flow</span></td><td></td><td></td><td></td><td></td><td><span class="class-tag gentle">Yin</span></td></tr>
      <tr><td class="time">9:30am</td><td><span class="class-tag gentle">Slow flow</span></td><td></td><td></td><td><span class="class-tag flow">vinyasa flow</span></td><td></td><td></td><td></td></tr>
      <tr><td class="time">10:30am</td><td></td><td></td><td></td><td></td><td></td><td><span class="class-tag prenatal">pregnancy*</span></td><td></td></tr>
      <tr><td class="time">11:00am</td><td></td><td><span class="class-tag prenatal">mum + baby*</span></td><td></td><td><span class="class-tag prenatal">mum + baby*</span></td><td></td><td></td><td></td></tr>
      <tr><td class="time">12:15pm</td><td></td><td></td><td><span class="class-tag youth">kids 8-12*</span></td><td><span class="class-tag prenatal">pregnancy</span></td><td></td><td></td><td></td></tr>
      <tr><td class="time">4:00pm</td><td></td><td></td><td><span class="class-tag youth">Teens 12-16*</span></td><td><span class="class-tag youth">kids 5-7*</span></td><td></td><td><span class="class-tag flow">vinyasa flow</span></td><td></td></tr>
      <tr><td class="time">4:45pm</td><td></td><td></td><td></td><td></td><td></td><td></td><td></td></tr>
      <tr><td class="time">5:00pm</td><td></td><td></td><td></td><td><span class="class-tag youth">teens 12-16*</span></td><td></td><td></td><td></td></tr>
      <tr><td class="time">6:00pm</td><td><span class="class-tag prenatal">Pregnancy</span></td><td><span class="class-tag flow">vinyasa flow</span></td><td><span class="class-tag gentle">slow flow</span></td><td></td><td><span class="class-tag gentle">Flow + restore</span></td><td></td><td></td></tr>
      <tr><td class="time">6:15pm</td><td></td><td></td><td></td><td><span class="class-tag prenatal">pregnancy*</span></td><td></td><td></td><td></td></tr>
      <tr><td class="time">7:30pm</td><td><span class="class-tag flow">vinyasa flow</span></td><td><span class="class-tag prenatal">pregnancy*</span></td><td><span class="class-tag gentle">yin + restore</span></td><td><span class="class-tag special">women's wellness*</span></td><td></td><td></td><td></td></tr>
    </tbody>
  </table>
</section>

</body>
</html>
```